Business Card

I need a business card that really pops for a potential customer or person who refers a personal injury lead. I want to highlight our office locations, but only address that needs to be on the card is my office's main address. I want a sleek, modern and minimalist design.

```html
<!DOCTYPE html>
<html lang="en">
<head>
<meta charset="utf-8">
<title>Prairie Injury Lawyers – Business Card</title>
<link href="https://fonts.googleapis.com/css2?family=Montserrat:wght@600&display=swap" rel="stylesheet">
<style>
  :root {
    --canvas: #efefef;
    --card-light: #ffffff;
    --card-dark: #3a3a3a;
    --card-dark-edge: #333333;
    --ink: #333333;
    --ink-reverse: #ffffff;
  }
  * { margin: 0; padding: 0; box-sizing: border-box; }
  html, body {
    width: 1200px;
    height: 1200px;
    overflow: hidden;
    background: var(--canvas);
  }
  .canvas {
    position: relative;
    width: 1200px;
    height: 1200px;
  }
  .card {
    position: absolute;
    left: 162px;
    width: 876px;
    height: 525px;
    overflow: hidden;
  }
  .card--front { top: 59px; background: var(--card-light); color: var(--ink); }
  .card--back { top: 616px; color: var(--ink-reverse); }

  .card__texture {
    position: absolute;
    inset: 0;
    width: 100%;
    height: 100%;
    background: radial-gradient(ellipse at 40% 45%, var(--card-dark) 0%, var(--card-dark-edge) 100%);
  }

  .firm-name {
    position: absolute;
    left: 0;
    right: 0;
    text-align: center;
    font-family: "Montserrat", "Helvetica Neue", sans-serif;
    font-weight: 600;
    font-size: 50px;
    letter-spacing: 1px;
    line-height: 1;
    white-space: nowrap;
  }
  .card--front .firm-name { top: 140px; }
  .card--back .firm-name { top: 237px; }

  .card__rule {
    position: absolute;
    left: 76px;
    right: 77px;
    top: 313px;
    height: 3px;
    background: var(--ink);
  }

  .contacts {
    position: absolute;
    top: 378px;
    list-style: none;
    font-family: "Montserrat", "Helvetica Neue", sans-serif;
    font-weight: 600;
    font-size: 18.5px;
    letter-spacing: 0.3px;
    line-height: 1;
  }
  .contacts li {
    display: flex;
    align-items: center;
    height: 22px;
    margin-bottom: 13px;
    gap: 18px;
  }
  .contacts--left { left: 76px; }
  .contacts--right { right: 76px; }
  .contacts--right li { justify-content: flex-end; }
  .contacts svg {
    width: 12px;
    height: 12px;
    fill: var(--ink);
    flex: none;
  }
</style>
</head>
<body>
<main class="canvas">

  <section class="card card--front" aria-label="Business card front">
    <h1 class="firm-name">Prairie Injury Lawyers</h1>
    <div class="card__rule"></div>

    <ul class="contacts contacts--left">
      <li>
        <svg viewBox="0 0 24 24" aria-hidden="true"><path d="M6.6 10.8a15.1 15.1 0 0 0 6.6 6.6l2.2-2.2c.3-.3.7-.4 1-.2 1.1.4 2.3.6 3.6.6.6 0 1 .4 1 1V20c0 .6-.4 1-1 1C10.6 21 3 13.4 3 4c0-.6.4-1 1-1h3.5c.6 0 1 .4 1 1 0 1.3.2 2.5.6 3.6.1.3 0 .7-.2 1z"/></svg>
        <span>+111 4380 0000</span>
      </li>
      <li>
        <svg viewBox="0 0 24 24" aria-hidden="true"><path d="M6.6 10.8a15.1 15.1 0 0 0 6.6 6.6l2.2-2.2c.3-.3.7-.4 1-.2 1.1.4 2.3.6 3.6.6.6 0 1 .4 1 1V20c0 .6-.4 1-1 1C10.6 21 3 13.4 3 4c0-.6.4-1 1-1h3.5c.6 0 1 .4 1 1 0 1.3.2 2.5.6 3.6.1.3 0 .7-.2 1z"/></svg>
        <span>+222 7702 0000</span>
      </li>
    </ul>

    <ul class="contacts contacts--right">
      <li>
        <span>+852 0000 6464</span>
        <svg viewBox="0 0 24 24" aria-hidden="true"><path d="M7 2h10v5H7zM4 8h16a2 2 0 0 1 2 2v7h-4v5H6v-5H2v-7a2 2 0 0 1 2-2zm4 8v4h8v-4zm10-5.5a1 1 0 1 0 0 2 1 1 0 0 0 0-2z"/></svg>
      </li>
      <li>
        <span>marketing@prairieinjury.com</span>
        <svg viewBox="0 0 24 24" aria-hidden="true"><path d="M2 5h20v2.2l-10 6.3L2 7.2zm0 4.6l10 6.3 10-6.3V19H2z"/></svg>
      </li>
    </ul>
  </section>

  <section class="card card--back" aria-label="Business card back">
    <div class="card__texture" role="img" aria-label="Subtle grey topographic contour-line texture"></div>
    <p class="firm-name">Prairie Injury Lawyers</p>
  </section>

</main>
</body>
</html>
```